TR Stationery - Modern Contemporary

Develop modern template for Letterhead and Stationery (business card, letterhead, envelopes) using the TR Logo and Icon

Colors
0054AA
0677BA
7BADD7
CADEEF
E8F1F8
00AB8E
00BBA5
67D7C9
C6EFE9
E9F9F6
EE7325
F08F49
F5BC92
FAE3D3
FDF4ED
6B429C
8869AF
B7A5CE
E3DAEB
F3F0F8

```html
<!DOCTYPE html>
<html lang="en">
<head>
<meta charset="utf-8">
<title>TR Stationery</title>
<link href="https://fonts.googleapis.com/css2?family=Fraunces:opsz,wght@9..144,500&display=swap" rel="stylesheet">
<style>
  :root {
    --backdrop: #7a7a7a;
    --paper: #efefef;
    --navy: #2a2f4d;
    --orange: #f58025;
    --flap-line: #d8d8d8;
  }
  html, body { margin: 0; padding: 0; overflow: hidden; }
  body {
    width: 1200px; height: 930px;
    background: var(--backdrop);
    position: relative;
    font-family: "Fraunces", Georgia, serif;
  }
  .sheet {
    position: absolute;
    background: var(--paper);
    box-shadow: 0 3px 8px rgba(0,0,0,0.25);
    overflow: hidden;
  }
  .sheet svg.art { position: absolute; inset: 0; width: 100%; height: 100%; }
  .wordmark {
    position: absolute;
    margin: 0;
    color: var(--navy);
    font-weight: 500;
    line-height: 1;
    letter-spacing: 0.02em;
    display: flex; align-items: center;
    white-space: nowrap;
  }
  .wordmark .dot {
    display: inline-block;
    width: 0.22em; height: 0.22em;
    border-radius: 50%;
    background: var(--orange);
    margin-left: 0.12em;
  }

  .letterhead { left: 149px; top: 174px; width: 425px; height: 599px; }
  .letterhead .wordmark { left: 33px; top: 30px; font-size: 28px; }

  .card-front { left: 612px; top: 117px; width: 206px; height: 118px; }
  .card-front .wordmark { right: 10px; bottom: 10px; font-size: 22px; }

  .card-back { left: 846px; top: 117px; width: 207px; height: 118px; }

  .envelope { left: 612px; top: 262px; width: 439px; height: 211px; background: #f4f4f4; }
  .envelope .wordmark { left: 31px; top: 145px; font-size: 30px; }

  .notebook { left: 637px; top: 505px; width: 414px; height: 307px; }
  .notebook .wordmark { left: 0; right: 26px; top: 130px; justify-content: center; font-size: 54px; }
</style>
</head>
<body>

<section class="sheet letterhead" aria-label="Letterhead">
  <svg class="art" viewBox="0 0 425 599" preserveAspectRatio="none">
    <path fill="var(--navy)" d="M0 0H422V35H300C262 35 258 10 224 10H0Z"/>
    <path fill="var(--orange)" d="M0 9H85C70 17 55 22 30 22H0Z"/>
    <path fill="var(--navy)" d="M0 599H422V569H109C82 569 88 591 65 591H0Z"/>
    <g class="contact-icons">
      <circle cx="184" cy="573" r="4.5" fill="var(--orange)"/>
      <path d="M184 570.6a1.6 1.6 0 0 1 1.6 1.6c0 1.2-1.6 3-1.6 3s-1.6-1.8-1.6-3a1.6 1.6 0 0 1 1.6-1.6z" fill="#fff"/>
      <circle cx="272" cy="573" r="4.5" fill="var(--orange)"/>
      <rect x="269.8" y="571.6" width="4.4" height="3" rx="0.8" fill="#fff"/>
      <rect x="270.8" y="570.6" width="2.4" height="1.2" rx="0.5" fill="#fff"/>
      <circle cx="359" cy="573" r="4.5" fill="var(--orange)"/>
      <circle cx="359" cy="573" r="2.4" fill="none" stroke="#fff" stroke-width="0.7"/>
      <path d="M356.6 573h4.8M359 570.6v4.8" stroke="#fff" stroke-width="0.5"/>
    </g>
  </svg>
  <h1 class="wordmark">TR<span class="dot"></span></h1>
</section>

<section class="sheet card-front" aria-label="Business card front">
  <p class="wordmark">TR<span class="dot"></span></p>
</section>

<section class="sheet card-back" aria-label="Business card back">
  <svg class="art" viewBox="0 0 207 118" preserveAspectRatio="none">
    <path fill="var(--navy)" d="M0 5H203V20H150C128 20 130 9 108 9H0Z"/>
    <path fill="var(--orange)" d="M0 9H38C32 12 26 14 16 14H0Z"/>
  </svg>
</section>

<section class="sheet envelope" aria-label="Envelope">
  <svg class="art" viewBox="0 0 439 211" preserveAspectRatio="none">
    <path fill="#f7f7f7" stroke="var(--flap-line)" stroke-width="1" d="M1 0L14 48Q17 57 30 57H410Q422 57 425 48L438 0Z"/>
    <path fill="none" stroke="var(--flap-line)" stroke-width="0.8" d="M18 60L2 200"/>
    <path fill="var(--navy)" d="M0 211H438V175H380C330 175 330 201 244 201H0Z"/>
    <path fill="var(--orange)" d="M0 188H40C64 188 78 194 88 201H0Z"/>
  </svg>
  <p class="wordmark">TR<span class="dot"></span></p>
</section>

<section class="sheet notebook" aria-label="Notebook cover">
  <svg class="art" viewBox="0 0 414 307" preserveAspectRatio="none">
    <path fill="var(--navy)" d="M388 0H412V307H405V122C405 100 388 95 388 75Z"/>
    <path fill="var(--orange)" d="M405 244V305H396V270C396 258 400 250 405 244Z"/>
  </svg>
  <p class="wordmark">TR<span class="dot"></span></p>
</section>

</body>
</html>
```